Shampoo and Shower Gel Packaging Design

I need a new packaging design for a men shampoo and shower gel bottle. The packaging must me black (black bottle/package) and the logo should be also monochrom.
For example, black matte bottle and black shiny logo on the packaging (not mandatory).
the design must contain maximum 3 colors.
1. black
2. white (text)
3. grey/dark blue/dark green (colors will be the difference between products parfumes/smell/scences.

Design must be minimalist/elegant/discrete.
Updates

Please check the photos i added for pure inspiration.

Target Market(s)

brand exclusively for MEN - premium clients

Industry/Entity Type

Cosmetics

Font styles to use
Sans Serif

Colors
1b1b1b
5c5c5c
aaaaaa
ffffff
3176b5

Requirements
Must have
• black background
• minimalist design

```html
<!DOCTYPE html>
<html lang="en">
<head>
<meta charset="utf-8">
<title>Orvane – Shower Gel Range</title>
<link rel="stylesheet" href="https://fonts.googleapis.com/css2?family=Questrial&display=swap">
<style>
  :root {
    --page: #ffffff;
    --body-dark: #2a2a2a;
    --body-mid: #353535;
    --cap-light: #e6e6e6;
    --cap-dark: #1b1b1b;
    --ink: #ffffff;
    --scent-green: #3a9a3f;
    --scent-grey: #aaaaaa;
    --scent-blue: #3176b5;
  }
  * { margin: 0; padding: 0; box-sizing: border-box; }
  html, body {
    width: 1200px; height: 848px; overflow: hidden;
    background: var(--page);
    font-family: "Questrial", "Century Gothic", sans-serif;
  }
  .range { position: relative; width: 1200px; height: 848px; }
  .bottle {
    position: absolute; top: 130px;
    width: 251px; height: 563px;
    color: var(--ink); text-align: center;
  }
  .bottle--green { left: 136px; --scent: var(--scent-green); }
  .bottle--grey  { left: 461px; --scent: var(--scent-grey); }
  .bottle--blue  { left: 787px; --scent: var(--scent-blue); }
  .bottle__shape { position: absolute; inset: 0; }
  .scent-mark {
    position: absolute; top: 145px; left: 50%;
    width: 40px; height: 40px; margin-left: -20px;
    border-radius: 50%; background: var(--scent);
  }
  .product-name {
    position: absolute; top: 206px; left: 0; right: 0;
    font-size: 27px; line-height: 1;
  }
  .product-rule {
    position: absolute; top: 242px; left: 77px;
    width: 97px; height: 2px; background: var(--scent);
  }
  .product-type {
    position: absolute; top: 250px; left: 0; right: 0;
    font-size: 12px;
  }
  .product-scent {
    position: absolute; top: 292px; left: 0; right: 0;
    font-size: 12px; line-height: 16px;
  }
  .brand {
    position: absolute; top: 382px; left: 0; right: 0;
    display: flex; flex-direction: column; align-items: center; gap: 10px;
  }
  .brand__dot { width: 16px; height: 16px; border-radius: 50%; background: var(--ink); }
  .brand__name { font-size: 20px; letter-spacing: 7px; padding-left: 7px; line-height: 1; }
  .volume {
    position: absolute; top: 516px; left: 50%;
    width: 50px; height: 28px; margin-left: -25px;
    border: 1px solid var(--ink); border-radius: 50%;
    font-size: 11px; line-height: 26px;
  }
</style>
</head>
<body>
<main class="range">
  <svg width="0" height="0" aria-hidden="true" style="position:absolute">
    <defs>
      <linearGradient id="cap-shade" x1="0" x2="1" y1="0" y2="0">
        <stop offset="0" stop-color="#f0f0f0"/>
        <stop offset="0.35" stop-color="#5c5c5c"/>
        <stop offset="0.65" stop-color="#1b1b1b"/>
        <stop offset="1" stop-color="#d8d8d8"/>
      </linearGradient>
      <linearGradient id="body-shade" x1="0" x2="1" y1="0" y2="0">
        <stop offset="0" stop-color="#262626"/>
        <stop offset="0.5" stop-color="#363636"/>
        <stop offset="1" stop-color="#2a2a2a"/>
      </linearGradient>
    </defs>
  </svg>

  <article class="bottle bottle--green">
    <svg class="bottle__shape" viewBox="0 0 251 563" aria-hidden="true">
      <rect x="77" y="0" width="97" height="94" fill="url(#cap-shade)"/>
      <path d="M0 200 C0 130 44 92 125.5 92 C207 92 251 130 251 200 V541 Q251 563 229 563 H22 Q0 563 0 541 Z" fill="url(#body-shade)"/>
    </svg>
    <span class="scent-mark"></span>
    <h2 class="product-name">Name</h2>
    <span class="product-rule"></span>
    <p class="product-type">Shower gel</p>
    <p class="product-scent">For Men<br>with<br>Fragrance 1</p>
    <div class="brand"><span class="brand__dot"></span><span class="brand__name">ORVANE</span></div>
    <p class="volume">300 ml</p>
  </article>

  <article class="bottle bottle--grey">
    <svg class="bottle__shape" viewBox="0 0 251 563" aria-hidden="true">
      <rect x="77" y="0" width="97" height="94" fill="url(#cap-shade)"/>
      <path d="M0 200 C0 130 44 92 125.5 92 C207 92 251 130 251 200 V541 Q251 563 229 563 H22 Q0 563 0 541 Z" fill="url(#body-shade)"/>
    </svg>
    <span class="scent-mark"></span>
    <h2 class="product-name">Name</h2>
    <span class="product-rule"></span>
    <p class="product-type">Shower gel</p>
    <p class="product-scent">For Men<br>with<br>Fragrance 2</p>
    <div class="brand"><span class="brand__dot"></span><span class="brand__name">ORVANE</span></div>
    <p class="volume">300 ml</p>
  </article>

  <article class="bottle bottle--blue">
    <svg class="bottle__shape" viewBox="0 0 251 563" aria-hidden="true">
      <rect x="77" y="0" width="97" height="94" fill="url(#cap-shade)"/>
      <path d="M0 200 C0 130 44 92 125.5 92 C207 92 251 130 251 200 V541 Q251 563 229 563 H22 Q0 563 0 541 Z" fill="url(#body-shade)"/>
    </svg>
    <span class="scent-mark"></span>
    <h2 class="product-name">Name</h2>
    <span class="product-rule"></span>
    <p class="product-type">Shower gel</p>
    <p class="product-scent">For Men<br>with<br>Fragrance 3</p>
    <div class="brand"><span class="brand__dot"></span><span class="brand__name">ORVANE</span></div>
    <p class="volume">300 ml</p>
  </article>
</main>
</body>
</html>
```